Flyer-Design für Wechseljahresberatung
Zielgruppe
Zielgruppe: überwiegend Frauen
psycholog. Beratung in allen Lebenslagen, Wechseljahresberatung , Gesundheits- und Ernährungsberatung, Fastenbegleitung, Trauerbegleitung, Bachblütenberatung,Klangmassagen
Aufgabenstellung
es geht um einen 6teiligen Kurs für Frauen zwischen Ende 30 bis Ende 60. Beginn der Wechseljahre , Leben in den Wechseljahren und was kommt danach? Wie erkennt man (Frau) körperl. oder seelische Probleme, die schon auf We.jahre hindeuten? Wie gehe Frau damit um? Was passiert in den We.jahren? Was kann Frau selbst tun, um die We.jahre so gut wie möglich zu erleben? Im Kurs werden natürliche Hilfsmittel besprochen und erklärt, Entspannungstechniken vermittelt , die Psyche gestärkt, sodaß die betroffenen Frauen bei auftretenden We.jahrsproblemen die Möglichkeit haben,sich selbst helfen zu können.

```html
<!DOCTYPE html>
<html lang="de">
<head>
<meta charset="utf-8">
<title>Wechseljahre – Beratung und Begleitung</title>
<link href="https://fonts.googleapis.com/css2?family=Delius&family=Open+Sans:wght@400;600;700&display=swap" rel="stylesheet">
<style>
:root{
  --rose:#d1324f;
  --rose-text:#cf2f4c;
  --cream:#fcf0a2;
  --sun:#f7e07a;
  --ink:#2b2b2b;
  --muted:#555;
  --panel:#dedede;
  --box:#eef0f7;
  --white:#fff;
}
*{margin:0;padding:0;box-sizing:border-box}
html,body{width:1200px;height:2481px;overflow:hidden;background:var(--white)}
body{position:relative;font-family:"Open Sans",Arial,sans-serif;color:var(--ink)}
.page{position:absolute;left:28px;width:1144px;background:var(--white);overflow:hidden;box-shadow:0 0 4px rgba(0,0,0,.25)}
.page--front{top:14px;height:1214px}
.page--inside{top:1249px;height:1216px}
.abs{position:absolute}
.shapes{position:absolute;left:0;top:0}

/* front */
.advisor{left:41px;top:34px}
.advisor__name{font-size:30px;font-weight:400;color:var(--ink)}
.advisor__role{font-size:19px;line-height:26px;color:var(--muted)}
.note-box{left:41px;top:170px;width:484px;height:256px;background:var(--box)}
.services{left:41px;top:448px;list-style:none}
.services li{font-size:22px;color:var(--rose-text);height:74px;line-height:34px}
.services li::before{content:"• "}
.hero-title{left:574px;top:88px;width:570px;text-align:center;font-family:"Delius",cursive;color:var(--sun)}
.hero-title__main{font-size:56px;letter-spacing:3px;line-height:64px}
.hero-title__sub{font-size:25px;letter-spacing:2px;margin-top:12px}
.photo-portrait{left:574px;top:330px;width:570px;height:650px;
  background:radial-gradient(ellipse at 68% 45%,rgba(124,138,176,.75) 0%,rgba(124,138,176,.35) 22%,transparent 45%),
  linear-gradient(180deg,#c9d98a 0%,#e8eec0 35%,#b8d060 70%,#8fbf2a 100%)}
.brand{left:39px;top:1060px;display:flex;align-items:center;gap:12px}
.brand__dot{width:22px;height:22px;border-radius:50%;background:var(--ink)}
.brand__name{font-size:28px;font-weight:600;color:var(--ink)}
.contact{left:204px;top:1030px;font-size:15.5px;line-height:20px;color:var(--ink);font-style:normal}
.contact strong{font-weight:700}
.contact__gap{height:14px}
.contact__row span{display:inline-block;width:62px}
.topics{left:640px;top:1000px;width:440px;text-align:center;font-family:"Delius",cursive;font-size:24px;color:var(--rose-text);line-height:29px}
.topics p{margin-bottom:15px}

/* inside */
.section-title{left:45px;top:32px;font-size:30px;line-height:36px;font-weight:400;color:var(--white)}
.intro{left:46px;top:124px;width:486px;font-size:18.6px;line-height:28.2px;text-align:justify}
.intro p{margin-bottom:28px}
.intro ul{list-style:none}
.course{left:613px;top:70px;width:492px;height:373px;background:var(--panel);padding:14px 25px;font-size:19px;line-height:26px}
.course h2{font-size:26px;font-weight:400;margin-bottom:12px}
.course h3{font-size:19px;font-weight:700;margin-top:12px}
.course p.signup{margin-top:12px}
.details{left:613px;top:472px;width:492px;font-size:18.6px;line-height:28.2px;text-align:justify}
.details p{margin-bottom:28px}
.details p.last{margin-top:56px}
.photo-forest{left:0;top:840px;width:1144px;height:376px;
  background:radial-gradient(ellipse at 52% 40%,#fffbe0 0%,#f2f28a 12%,transparent 40%),
  linear-gradient(180deg,#7fae3a 0%,#a9c84a 45%,#5f8a2c 80%,#4a6a22 100%)}
.tagline{left:600px;top:1096px;width:520px;text-align:center;font-family:"Delius",cursive;font-size:28px;line-height:33px;color:var(--white)}
</style>
</head>
<body>

<section class="page page--front">
  <div class="abs photo-portrait" role="img" aria-label="Foto: lächelnde Frau mittleren Alters sitzt im sonnigen Gras"></div>
  <svg class="shapes" width="1144" height="1214" viewBox="0 0 1144 1214" aria-hidden="true">
    <path d="M574 0H1144V318Q860 322 574 368Z" fill="var(--rose)"/>
    <path d="M574 368Q860 322 1144 318V334Q860 336 574 382Z" fill="var(--sun)"/>
    <path d="M574 382Q860 336 1144 334V346Q860 346 574 392Z" fill="var(--white)"/>
    <path d="M0 962Q600 955 1144 905V1214H0Z" fill="var(--white)"/>
    <path d="M0 976Q600 965 1144 915V1214H0Z" fill="var(--cream)"/>
  </svg>

  <header class="abs advisor">
    <h1 class="advisor__name">Marlene Hoffbauer-Lenz</h1>
    <p class="advisor__role">Gesundheitsberaterin</p>
    <p class="advisor__role">Psycholog. Beraterin</p>
    <p class="advisor__role">Wechseljahresberaterin</p>
  </header>
  <div class="abs note-box"></div>
  <ul class="abs services">
    <li>Psycholog. Beratung in allen Lebenslagen</li>
    <li>Wechseljahresberatung</li>
    <li>Gesundheits- und Ernährungsberatung</li>
    <li>Fastenbegleitung</li>
    <li>Trauerbegleitung</li>
    <li>Bachblütenberatung</li>
    <li>Klangmassagen</li>
  </ul>

  <div class="abs hero-title">
    <div class="hero-title__main">WECHSELJAHRE</div>
    <div class="hero-title__sub">BERATUNG UND BEGLEITUNG</div>
  </div>

  <div class="abs brand"><span class="brand__dot"></span><span class="brand__name">Lunara</span></div>
  <address class="abs contact">
    <strong>Lunara</strong><br>
    Marlene Hoffbauer-Lenz<br>
    Lindenweg 12<br>
    6400AB Beekdal / NL
    <div class="contact__gap"></div>
    <div class="contact__row"><span>Telefon:</span>0241 / 00 00 12 34</div>
    <div class="contact__row"><span>oder</span>+31 (0)45 / 0 00 98 76</div>
    <div class="contact__row"><span>Mail:</span>mondhalmkreise@entwurfhafen.de</div>
  </address>

  <div class="abs topics">
    <p>Vorbereitung auf die Wechseljahre</p>
    <p>Leben in den Wechseljahren</p>
    <p>Möglichkeiten der Selbsthilfe<br>bei entsprechenden Beschwerden</p>
    <p>Was kommt danach?</p>
  </div>
</section>

<section class="page page--inside">
  <div class="abs photo-forest" role="img" aria-label="Foto: sonnendurchfluteter grüner Laubwald"></div>
  <svg class="shapes" width="1144" height="1216" viewBox="0 0 1144 1216" aria-hidden="true">
    <path d="M0 0H1144V8C820 18 420 56 0 92Z" fill="var(--rose)"/>
    <path d="M0 830H1144V870Q600 850 0 820Z" fill="var(--white)"/>
    <path d="M0 834Q600 856 1144 876V888Q600 870 0 848Z" fill="var(--sun)"/>
    <path d="M0 848Q600 870 1144 888V910Q600 892 0 870Z" fill="var(--white)"/>
  </svg>

  <h2 class="abs section-title">Wechseljahre</h2>

  <div class="abs intro">
    <p>Im Alter von Ende 30 bis ca. 60 Jahren erfolgt eine hor&shy;monelle Umstellung des weiblichen Körpers - die ver&shy;unsichern und belasten können, die sog. Wechseljahre. Sie bringen körperliche und seelische Veränderungen mit sich, die verunsichern können und von uns Frauen in unterschiedlicher Intensität und Dauer erlebt werden. Viele Fragen ergeben sich und somit auch der Wunsch nach Unterstützung.</p>
    <p>So individuell die Symptome sind, so vielfältig sind auch die Lösungen.</p>
    <p>Gleichzeitig erleben auch viele von uns Einschnitte in ihren Beziehungen, die Kinder gehen aus dem Haus oder es fehlt der Sinn im Arbeitsalltag.</p>
    <div style="margin-bottom:28px">Es tauchen Fragen auf, wie:
      <ul>
        <li>• Was will ich eigentlich?</li>
        <li>• Wie möchte ich mein Leben noch gestalten?</li>
        <li>• Habe ich den Mut und die Kraft etwas zu ändern?</li>
      </ul>
    </div>
    <p>In solchen Zeiten ist es wichtig, unsere Aufmerksam&shy;keit auf uns selbst und nach Innen zu richten.</p>
  </div>

  <aside class="abs course">
    <h2>Wechseljahre - Start Kurs 2017</h2>
    <p>11. September - 16. Oktober<br>6 x Montags 19.00 - 20.30 Uhr</p>
    <h3>Kursbeitrag</h3>
    <p>139,-- pro Teilnehmerin</p>
    <h3>Kursort</h3>
    <p>Linden-Apotheke - Seminarraum<br>Brunnenstraße 14<br>52100 Mühlbach-Au</p>
    <p class="signup">Anmeldung gern in der Linden-Apotheke<br>oder telef. in meiner Praxis.</p>
  </aside>

  <div class="abs details">
    <p>In diesem Kurs möchte ich Ihnen die Wechseljahre mit all ihren schönen, aber auch problematischeren Seiten etwas näher bringen.<br>Sie lernen Entspannungstechniken und andere Hilfsmit&shy;tel kennen, die sie bei Bedarf gezielt einsetzen können.</p>
    <p>Unser Ziel ist, die Wechseljahre so natürlich wie möglich erleben zu dürfen.</p>
    <p class="last">Sollten Sie eine Einzelberatung vorziehen, stehe ich Ihnen gern nach tel. Terminabsprache in meiner Praxis zur Verfügung.</p>
  </div>

  <div class="abs tagline">Aufmerksamkeit auf sich selbst<br>und nach Innen</div>
</section>

</body>
</html>
```